Home Renovation Business needs a logo and business card design

I need a logo design for my home renovation company. I work hard to provide quality work for a fair price. I want a clean design that has something to make it pop and catch the eye. It should have somewhat of a modern feel to it. You can check out my website at www.kbbuildworks.com to see some examples of the type of work I do.
Updates

Hi Everyone,

For some reason, not all my information was posted. I would like the following contact information included in the design:

Phone: 365.417.9826        Email: kdrosmol@maplepost.ca        Website: www.kbbuildworks.com

Also, if you would like to include a list of the services I offer, then I'd like the card to be double sided. I provide the following services: Full kitchen, basement and bathroom renovations. Tile, laminate and hardwood installation. Decks, fences and sheds. Windows and doors.

Industry/Entity Type

Business

Requirements
Must have
• I want the following information listed on the card:
• KD Buildworks
• Kyle Drosmolen
• 365.417.9826
• kdrosmol@maplepost.ca
• www.kbbuildworks.com
Nice to have
• If you want you could also include the list of services I provide. If you include this list feel free to make the card double sided.
• Kitchen, bathroom and basement renovations
• Flooring installation
• Decks, fences and sheds
• Windows and doors
• I am not 100% sure if I want to include this on the card or not.

```html
<!DOCTYPE html>
<html lang="en">
<head>
<meta charset="utf-8">
<title>KD Buildworks – Business Card</title>
<link rel="stylesheet" href="https://fonts.googleapis.com/css2?family=Arimo:wght@400;700&display=swap">
<style>
  :root {
    --bg: #dcd7cf;
    --card-black: #161616;
    --card-black-light: #2c2c2c;
    --brand-red: #e21f2b;
    --ink-white: #ffffff;
    --ink-grey: #d6d6d6;
  }
  * { margin: 0; padding: 0; box-sizing: border-box; }
  html, body {
    width: 1200px; height: 902px; overflow: hidden;
    background: var(--bg);
    font-family: "Arimo", Arial, sans-serif;
  }
  .sheet {
    position: relative; width: 1200px; height: 902px;
    display: flex; flex-direction: column; align-items: center;
    justify-content: center; gap: 42px;
  }
  .card {
    position: relative; width: 700px; height: 400px; overflow: hidden;
    background: linear-gradient(160deg, var(--card-black-light) 0%, var(--card-black) 55%, #0c0c0c 100%);
    box-shadow: 0 8px 22px rgba(0,0,0,0.25);
  }
  .card svg.card-art { position: absolute; inset: 0; width: 100%; height: 100%; }

  /* Front */
  .brand {
    position: absolute; right: 78px; top: 74px;
    display: flex; align-items: center; gap: 14px;
  }
  .brand-mark { width: 26px; height: 26px; background: var(--brand-red); flex: none; }
  .brand-name {
    font-weight: 700; font-size: 46px; line-height: 1; color: var(--ink-white);
    letter-spacing: 0.5px; white-space: nowrap;
  }
  .brand-web {
    position: absolute; right: 112px; top: 138px;
    font-size: 20px; letter-spacing: 4px; color: var(--ink-grey); white-space: nowrap;
  }
  .brand-web .domain { color: var(--brand-red); }
  .contact {
    position: absolute; left: 46px; top: 276px;
    display: flex; flex-direction: column; gap: 18px;
    color: var(--ink-white); font-size: 27px; line-height: 1;
  }
  .contact-line { display: flex; align-items: center; gap: 16px; white-space: nowrap; }
  .contact-line svg { width: 26px; height: 26px; flex: none; }

  /* Back */
  .service-text {
    fill: var(--ink-white); font-family: "Arimo", Arial, sans-serif;
    font-size: 21px; text-anchor: middle;
  }
</style>
</head>
<body>
<main class="sheet">

  <section class="card card-front" aria-label="Card front">
    <svg class="card-art" viewBox="0 0 700 400" aria-hidden="true">
      <path d="M0 236 L565 226 Q612 225 612 268 L612 400 L0 400 Z" fill="var(--brand-red)"/>
      <path d="M0 236 L565 226 Q612 225 612 268 L612 290 Q400 250 0 300 Z" fill="#ffffff" opacity="0.08"/>
    </svg>
    <div class="brand">
      <span class="brand-mark"></span>
      <span class="brand-name">KD Buildworks</span>
    </div>
    <div class="brand-web">www.<span class="domain">kbbuildworks</span>.com</div>
    <div class="contact">
      <div class="contact-line">
        <svg viewBox="0 0 24 24" aria-hidden="true"><rect x="2" y="5" width="20" height="14" fill="#fff"/><path d="M2 5 L12 13 L22 5" fill="none" stroke="#e21f2b" stroke-width="1.6"/></svg>
        <span>kdrosmol@maplepost.ca</span>
      </div>
      <div class="contact-line">
        <svg viewBox="0 0 24 24" aria-hidden="true"><path d="M6.6 10.8a15 15 0 0 0 6.6 6.6l2.2-2.2c.3-.3.7-.4 1-.2 1.1.4 2.3.6 3.6.6.6 0 1 .4 1 1V20c0 .6-.4 1-1 1A17 17 0 0 1 3 4c0-.6.4-1 1-1h3.5c.6 0 1 .4 1 1 0 1.3.2 2.5.6 3.6.1.3 0 .7-.2 1z" fill="#fff"/></svg>
        <span>365.417.9826</span>
      </div>
    </div>
  </section>

  <section class="card card-back" aria-label="Card back with services">
    <svg class="card-art" viewBox="0 0 700 400">
      <g transform="rotate(-10 350 200)">
        <rect x="-120" y="112" width="940" height="46" fill="var(--brand-red)"/>
        <rect x="-120" y="168" width="940" height="46" fill="var(--brand-red)"/>
        <rect x="-120" y="224" width="940" height="46" fill="var(--brand-red)"/>
        <rect x="-120" y="280" width="940" height="46" fill="var(--brand-red)"/>
        <text class="service-text" x="350" y="142">full kitchen, basement and bathroom renovations</text>
        <text class="service-text" x="350" y="198">decks, fences and sheds</text>
        <text class="service-text" x="350" y="254">tile, laminate and hardwood installation</text>
        <text class="service-text" x="350" y="310">windows and doors</text>
      </g>
    </svg>
  </section>

</main>
</body>
</html>
```